Company raising consciousness thru leadership & self-awareness needs amazing Letterhead

We are a technology company that spun out of a consulting firm. We are waking people up in corporate America through surveys, leadership development, workshops and consulting. Getting employees to become self-aware and changing company culture through improved leadership and team effectiveness. We need Word letterhead for our proposals, handouts, and worksheets that match our brand standard, is fresh, and communicates trust, credibility and professionalism.

Target Market(s)

Our target clients are other businesses, and executive leaders and C-suite leaders in those companies.

Font styles to use
Sans Serif

Requirements
Must have
• A Word template we can use for handouts, proposals, executive summary, project management documents, and letters. We need our logo. Please add page number and date on the footer. Must match the theme of our new website in look and feel to match the brand we are trying to promote. Use the colors from our brand standard document I submitted.

```html
<!DOCTYPE html>
<html lang="en">
<head>
<meta charset="utf-8">
<title>Solvane Aware Leadership — Letterhead</title>
<link rel="stylesheet" href="https://fonts.googleapis.com/css2?family=Montserrat:wght@500&family=Roboto:wght@400&display=swap">
<style>
  :root {
    --backdrop: #e9e9ea;
    --paper: #f7f7f7;
    --navy: #2e4379;
    --violet: #7b3f98;
    --ink: #3a3a3c;
    --muted: #8a8a8e;
    --watermark: rgba(123, 63, 152, 0.08);
  }
  * { box-sizing: border-box; margin: 0; padding: 0; }
  html, body { width: 1200px; height: 795px; overflow: hidden; background: var(--backdrop); }
  .letterhead {
    position: absolute; left: 333px; top: 20px;
    width: 534px; height: 755px;
    background: var(--paper);
    box-shadow: 0 2px 10px rgba(0,0,0,0.08);
    overflow: hidden;
  }
  .brand-mark {
    position: absolute; left: 40px; top: 30px;
    display: flex; align-items: center; gap: 8px;
    font-family: "Montserrat", sans-serif; font-weight: 500;
    font-size: 10px; letter-spacing: 0.06em; color: var(--navy);
    text-transform: uppercase;
  }
  .brand-mark .dot { width: 22px; height: 22px; border-radius: 50%; background: var(--navy); }
  .contact-block {
    position: absolute; left: 374px; top: 36px;
    padding-left: 10px; border-left: 1px solid var(--violet);
    font-family: "Roboto", sans-serif; font-size: 8px; line-height: 10.5px; color: var(--ink);
  }
  .contact-line { display: flex; align-items: center; gap: 4px; }
  .contact-line svg { width: 7px; height: 7px; fill: var(--navy); flex: none; }
  .doc-fields {
    position: absolute; left: 398px; top: 124px; width: 112px;
    font-family: "Roboto", sans-serif; font-size: 8px; line-height: 14px; color: var(--ink);
  }
  .doc-field { display: flex; align-items: baseline; gap: 4px; }
  .doc-field .rule { flex: 1; border-bottom: 1px dotted var(--muted); }
  .watermark {
    position: absolute; left: 120px; top: 220px; width: 320px; height: 320px;
    border-radius: 50%; border: 6px solid var(--watermark);
    display: flex; align-items: center; justify-content: center;
    font-family: "Montserrat", sans-serif; font-weight: 500; font-size: 22px;
    letter-spacing: 0.08em; color: var(--watermark); text-transform: uppercase; text-align: center;
  }
  .footer-name {
    position: absolute; right: 214px; bottom: 24px;
    font-family: "Montserrat", sans-serif; font-weight: 500;
    font-size: 12px; letter-spacing: 0.02em; color: var(--ink); text-transform: uppercase;
  }
  .footer-band { position: absolute; bottom: 0; height: 7px; }
  .footer-band.navy { left: 0; width: 61%; background: var(--navy); }
  .footer-band.violet {
    right: 0; width: 40%; height: 10px; background: var(--violet);
    clip-path: polygon(3px 0, 100% 0, 100% 100%, 0 100%, 0 30%);
  }
</style>
</head>
<body>
  <main class="letterhead">
    <div class="brand-mark"><span class="dot"></span>Solvane Aware Leadership</div>

    <address class="contact-block" style="font-style:normal">
      <div>48 Harborview Lane,</div>
      <div>Suite 310s, Easton,</div>
      <div>NY 11920</div>
      <div class="contact-line">
        <svg viewBox="0 0 10 10"><path d="M2 1l2 0 1 2-1.3 1a5 5 0 0 0 2.3 2.3L7 5l2 1v2a1 1 0 0 1-1 1A7 7 0 0 1 1 2a1 1 0 0 1 1-1z"/></svg>555-014-2288
      </div>
      <div class="contact-line">
        <svg viewBox="0 0 10 10"><path d="M0 2h10v6H0z M0 2l5 3.5L10 2" stroke="#f7f7f7" stroke-width="0.8"/></svg>info@yourmail.com
      </div>
      <div class="contact-line">
        <svg viewBox="0 0 10 10"><circle cx="5" cy="5" r="5"/></svg>www.yourweb.com
      </div>
    </address>

    <div class="doc-fields">
      <div class="doc-field">Date <span class="rule"></span></div>
      <div class="doc-field">Page Numbers <span class="rule"></span></div>
    </div>

    <div class="watermark" aria-hidden="true">Solvane</div>

    <div class="footer-name">Solvane Aware Leadership</div>
    <div class="footer-band navy"></div>
    <div class="footer-band violet"></div>
  </main>
</body>
</html>
```